جمعية سنابل لصحة المرأة
جمعية سنابل لصحة المرأة Tamsara Women's health society
جمعية سنابل لصحة المرأة - Health
Creative Brief
Simple
Tamsara Women's health society
Riyadh Saudi Arabia
tamsara.whs@nelvomail.com
http://www.tamsara-example.org/
if also can have design on Mugs tshirts pins pens shopping bag thank you
same information but in arabic

```html
<!DOCTYPE html>
<html lang="en">
<head>
<meta charset="utf-8">
<title>Tamsara Women's health society – Business Card</title>
<link rel="stylesheet" href="https://fonts.googleapis.com/css2?family=Montserrat:wght@400;500;600&family=Cairo:wght@600&display=swap">
<style>
  :root {
    --stage: #4d4d4d;
    --paper: #ffffff;
    --purple: #7b3fa0;
    --lilac: #b48fd0;
    --soft: #9b6bbf;
    --ink-light: #ffffff;
  }
  * { margin: 0; padding: 0; box-sizing: border-box; }
  html, body { width: 1200px; height: 895px; overflow: hidden; }
  body {
    background: var(--stage);
    font-family: "Montserrat", Arial, sans-serif;
    position: relative;
  }
  .card {
    position: absolute;
    width: 560px;
    height: 320px;
    top: 287px;
    background: var(--paper);
    overflow: hidden;
  }
  .card--back { left: 26px; }
  .card--front { left: 614px; }
  .card__shape { position: absolute; inset: 0; }

  .brand {
    position: absolute;
    display: flex;
    align-items: center;
    gap: 12px;
    color: var(--purple);
    font-weight: 600;
    letter-spacing: 1px;
  }
  .brand__dot {
    width: 38px; height: 38px;
    border-radius: 50%;
    background: var(--soft);
  }
  .brand__name { font-size: 26px; }
  .card--back .brand { left: 62px; top: 138px; }
  .card--front .brand { left: 190px; top: 78px; }
  .society-ar {
    position: absolute;
    font-family: "Cairo", Arial, sans-serif;
    font-weight: 600;
    font-size: 13px;
    color: var(--purple);
    direction: rtl;
  }
  .card--back .society-ar { left: 112px; top: 182px; }
  .card--front .society-ar { left: 240px; top: 122px; }

  .contact {
    position: absolute;
    right: 26px;
    top: 30px;
    text-align: right;
    color: var(--ink-light);
  }
  .contact__name { font-size: 14px; font-weight: 500; letter-spacing: 1px; }
  .contact__role { font-size: 10px; margin-top: 2px; }
  .contact__address { font-size: 9.5px; line-height: 14px; margin-top: 38px; }
  .contact__list { list-style: none; margin-top: 18px; }
  .contact__list li {
    display: flex;
    justify-content: flex-end;
    align-items: center;
    gap: 8px;
    font-size: 9.5px;
    height: 18px;
  }
  .contact__list svg { width: 10px; height: 10px; fill: var(--ink-light); }

  .website {
    position: absolute;
    left: 0; right: 0;
    bottom: 30px;
    text-align: center;
    color: var(--ink-light);
    font-size: 16px;
    letter-spacing: 5px;
  }
</style>
</head>
<body>

<section class="card card--back">
  <svg class="card__shape" viewBox="0 0 560 320" aria-hidden="true">
    <path d="M296,0 C246,80 246,240 316,320 L560,320 L560,0 Z" fill="var(--lilac)"/>
    <path d="M314,0 C264,80 264,240 334,320 L560,320 L560,0 Z" fill="var(--purple)"/>
  </svg>
  <div class="brand"><span class="brand__dot"></span><span class="brand__name">TAMSARA</span></div>
  <p class="society-ar">جمعية سنابل لصحة المرأة</p>
  <div class="contact">
    <p class="contact__name">MARA KELLEN</p>
    <p class="contact__role">Managing Director</p>
    <p class="contact__address">27 Cedar Court, Level 4<br>Harbor Lane</p>
    <ul class="contact__list">
      <li>014 820 3157
        <svg viewBox="0 0 10 10"><path d="M2,0.5 L4,2.5 L3,3.8 C3.7,5.2 4.8,6.3 6.2,7 L7.5,6 L9.5,8 L8.2,9.5 C4.5,9.2 0.8,5.5 0.5,1.8 Z"/></svg>
      </li>
      <li>014 820 3158
        <svg viewBox="0 0 10 10"><path d="M2.5,0 H7.5 V10 H2.5 Z M3.3,1 V8 H6.7 V1 Z"/></svg>
      </li>
      <li>014 820 3159
        <svg viewBox="0 0 10 10"><path d="M2,0 H8 V3 H10 V8 H0 V3 H2 Z M3,1 V3 H7 V1 Z M2,6 V10 H8 V6 Z"/></svg>
      </li>
      <li>mara@tamsara-example.org
        <svg viewBox="0 0 10 10"><path d="M0,2 H10 V8 H0 Z M1,2.8 L5,5.6 L9,2.8 V3.6 L5,6.4 L1,3.6 Z" fill-rule="evenodd"/></svg>
      </li>
      <li>www.tamsara-example.org
        <svg viewBox="0 0 10 10"><circle cx="5" cy="5" r="4.5"/></svg>
      </li>
    </ul>
  </div>
</section>

<section class="card card--front">
  <svg class="card__shape" viewBox="0 0 560 320" aria-hidden="true">
    <path d="M0,196 Q280,146 560,186 L560,320 L0,320 Z" fill="var(--lilac)"/>
    <path d="M0,212 Q280,164 560,202 L560,320 L0,320 Z" fill="var(--purple)"/>
  </svg>
  <div class="brand"><span class="brand__dot"></span><span class="brand__name">TAMSARA</span></div>
  <p class="society-ar">جمعية سنابل لصحة المرأة</p>
  <p class="website">www.tamsara-example.org</p>
</section>

</body>
</html>
```